Vital Spark Electrical in need of a business card design

We need a new business card designed for our electrical business. We have a logo already which I will attach below.
Would like the business card to be..
-BLACK background preferably, possibly white back ground behind logo if colours clash.
-White & Blue (logo blue) text
Something that makes the logo pop, & a modern look. Possibly minimal clean format.

REQUIRE:
-Logo on front & back

TEXT TO INCLUDE (ON ONE SIDE):

Tom Harlow
Director/Electrician
M: 0417 365 208
E:info@vitalsparkelectrical-example.com.au
W:www.vitalsparkelectrical-example.com.au
R.E.C 57318

Custom/New Homes
Renovations
Commercial Office/Shop Fit-outs
Communications & Security Cameras
Electric Vehicle Chargers
Airconditioning
Updates

Requirements
Nice to have
• Possibly even lighten the grey shades for the words 'Vital' & 'Spark' to be more easily read on a black background.

```html
<!DOCTYPE html>
<html lang="en">
<head>
<meta charset="utf-8">
<title>Vital Spark Electrical – Services Card</title>
<link rel="stylesheet" href="https://fonts.googleapis.com/css2?family=Montserrat:wght@300;600&display=swap">
<style>
  :root {
    --card-bg: #070707;
    --accent-blue: #05a8e0;
    --service-grey: #9a9a9a;
    --brand-grey: #6f7d88;
  }
  html, body {
    margin: 0;
    padding: 0;
    width: 1200px;
    height: 686px;
    overflow: hidden;
    background: var(--card-bg);
  }
  .card {
    position: relative;
    width: 1200px;
    height: 686px;
    overflow: hidden;
    background: var(--card-bg);
    font-family: "Montserrat", Arial, sans-serif;
  }
  .accent-bar {
    position: absolute;
    left: 0;
    top: 224px;
    width: 20px;
    height: 235px;
    background: var(--accent-blue);
  }
  .service-list {
    position: absolute;
    left: 71px;
    top: 210px;
    margin: 0;
    padding: 0;
    list-style: none;
  }
  .service-list li {
    font-weight: 300;
    font-size: 34px;
    line-height: 43px;
    letter-spacing: -1.1px;
    color: var(--service-grey);
    white-space: nowrap;
  }
  .brand {
    position: absolute;
    left: 737px;
    top: 318px;
    height: 50px;
    display: flex;
    align-items: center;
    gap: 16px;
  }
  .brand-mark {
    width: 40px;
    height: 40px;
    background: var(--accent-blue);
  }
  .brand-name {
    font-weight: 600;
    font-size: 26px;
    color: var(--brand-grey);
    white-space: nowrap;
  }
</style>
</head>
<body>
  <main class="card">
    <div class="accent-bar"></div>
    <ul class="service-list">
      <li>Custom/New Homes</li>
      <li>Renovations</li>
      <li>Commercial Office/Shop Fit-outs</li>
      <li>Communications &amp; Security Cameras</li>
      <li>Electric Vehicle Chargers</li>
      <li>Airconditioning</li>
    </ul>
    <div class="brand">
      <span class="brand-mark"></span>
      <span class="brand-name">Vital Spark Electrical</span>
    </div>
  </main>
</body>
</html>
```